OUTRAGEOUS NEW Website Coral Cove Massage

Need an OUTRAGEOUSLY BOLD, Brand New Website for a National Massage Chain with a Palm Beach Tropical Theme. Graphics/Fonts/Colors/Backgrounds should be EXTREMELY, EXTREMELY Bold, Attractive and Inviting. Not looking for same-old/same-old but a website that is memorable and vivid. Standard website designs will be rejected.
Creative, technically superior, artistic Web Designers with a GREAT eye feel free to compete and GIVE us your BEST!!!

Target Market(s)

Everyone

Industry/Entity Type

Massage

Number of Pages Required

5+ page

Requirements
Must have
• BIG, BOLD, BRIGHT COLORS/GRAPHICS/FONTS
Nice to have
• Name/Email address Lead Generation Box above the fold

```html
<!DOCTYPE html>
<html lang="en">
<head>
<meta charset="utf-8">
<title>Coral Cove Massage Centers</title>
<link rel="stylesheet" href="https://fonts.googleapis.com/css2?family=Roboto:wght@400;500;700&family=Courgette&display=swap">
<style>
:root{
  --red:#e8232a;
  --blue:#1f57ae;
  --dark:#313131;
  --white:#ffffff;
  --text:#444444;
  --sea:#35c2d2;
  --sand:#e8e1d6;
}
*{box-sizing:border-box;margin:0;padding:0}
html,body{width:884px;height:1200px;overflow:hidden}
body{position:relative;font-family:Roboto,Arial,sans-serif;color:var(--text);background:var(--sand)}
.beach-bg{position:absolute;inset:0;background:linear-gradient(180deg,#2f7fd0 0%,#6fb3e6 30%,#9fd7ee 45%,var(--sea) 55%,#7fd6d8 65%,var(--sand) 85%)}
.page{position:absolute;left:74px;top:26px;width:737px;height:980px;background:var(--white)}
.header{position:relative;height:119px}
.brand{position:absolute;left:18px;top:46px;display:flex;align-items:center;gap:8px;font-size:22px;font-weight:700;color:var(--blue)}
.brand .dot{width:22px;height:22px;border-radius:50%;background:var(--red)}
.call{position:absolute;right:10px;top:40px;display:flex;align-items:center;gap:12px}
.call-label{font-size:14px;font-weight:500;color:#222;letter-spacing:.3px}
.call-number{font-size:17px;font-weight:500;color:var(--red);letter-spacing:.6px;margin-top:3px}
.nav{height:40px;background:var(--red);display:flex;list-style:none}
.nav li{font-size:12px;color:var(--white);line-height:40px;padding:0 19px}
.nav li.active{background:var(--blue);width:74px;text-align:center;padding:0}
.hero{position:relative;height:316px;background:linear-gradient(110deg,#f1e6de 0%,#d9b39a 40%,#c99a80 70%,#e8cfc0 100%)}
.hero-caption{position:absolute;left:322px;top:118px;width:415px;height:105px;background:rgba(150,100,80,.45);padding:12px 8px 0 30px}
.hero-title{font-family:Courgette,cursive;font-size:26px;color:var(--blue);white-space:nowrap}
.hero-title span{color:var(--red)}
.hero-text{font-size:11.5px;color:var(--white);line-height:15px;margin-top:5px}
.services{position:absolute;top:508px;left:8px;display:flex;gap:23px}
.service{position:relative;width:225px;height:148px;border-radius:3px;overflow:hidden}
.service .photo{position:absolute;inset:0}
.service .label{position:absolute;left:0;right:0;bottom:0;height:37px;background:rgba(40,40,40,.7);color:var(--white);font-size:12px;font-weight:700;line-height:37px;padding-left:14px}
.service .go{position:absolute;right:14px;bottom:11px;width:15px;height:15px;border-radius:50%;background:var(--red)}
.welcome{position:absolute;left:16px;top:697px;width:420px}
.welcome h1{font-family:Courgette,cursive;font-weight:400;font-size:21px;color:#222;white-space:nowrap}
.welcome h1 .b{color:var(--blue)}.welcome h1 .r{color:var(--red)}
.welcome p{font-size:10px;line-height:17.6px;margin-top:14px;color:#444}
.btn{display:inline-block;background:var(--red);color:var(--white);font-size:10.5px;border-radius:2px}
.read-more{position:absolute;left:13px;top:851px;width:75px;height:27px;line-height:27px;text-align:center}
.booking{position:absolute;left:480px;top:689px;width:247px;height:233px;background:var(--blue);padding:0 10px}
.booking h2{color:var(--white);font-size:16px;font-weight:500;text-align:center;margin-top:13px}
.field{background:var(--white);height:29px;margin-top:11px;font-size:9.5px;color:#666;padding:10px 8px;border-radius:2px;width:226px}
.field.msg{height:51px;padding-top:7px}
.submit{margin-top:13px;width:75px;height:26px;line-height:26px;text-align:center}
.wave{position:absolute;left:0;top:0;width:884px;height:1200px}
.footer{position:absolute;left:73px;top:1030px;width:737px;color:var(--white)}
.col{position:absolute;top:0}
.col h3{color:var(--red);font-size:11px;font-weight:700;margin-bottom:9px}
.col p,.col li{font-size:9px;line-height:16.5px}
.links{display:grid;grid-template-columns:76px 80px;list-style:none;padding-left:3px}
.news-input{position:absolute;top:58px;left:2px;width:186px;height:28px;background:var(--white)}
.news-go{position:absolute;top:58px;left:165px;width:23px;height:28px;background:var(--red)}
.radios{position:absolute;top:91px;left:2px;display:flex;gap:14px;font-size:8.5px;align-items:center}
.radio{display:inline-block;width:10px;height:10px;border-radius:50%;background:var(--white);vertical-align:-2px;margin-right:6px}
.radio.on{box-shadow:inset 0 0 0 3px var(--white);background:#222}
.rule{position:absolute;left:74px;top:1155px;width:736px;height:1px;background:#666}
.copy{position:absolute;left:72px;top:1168px;font-size:10.5px;color:var(--white)}
.social{position:absolute;left:698px;top:1166px;display:flex;gap:8px}
.social span{width:22px;height:22px;border:1.5px solid var(--white);border-radius:50%}
</style>
</head>
<body>
<div class="beach-bg" role="img" aria-label="Tropical beach backdrop with palm leaves, blue sky and turquoise sea"></div>

<div class="page">
  <header class="header">
    <div class="brand"><span class="dot"></span>Coral Cove Massage</div>
    <div class="call">
      <svg width="36" height="36" viewBox="0 0 36 36" fill="none" stroke="#1f57ae" stroke-width="3" stroke-linecap="round">
        <path d="M8 6c-3 2-4 6-1 12s9 11 14 12c3 1 5-1 6-3l-5-5-3 2c-3-1-6-4-7-7l2-3-5-6z" fill="#1f57ae"/>
        <path d="M20 8a8 8 0 0 1 8 8"/><path d="M21 2a14 14 0 0 1 13 13"/>
      </svg>
      <div>
        <div class="call-label">Contact Us Today!</div>
        <div class="call-number">(0142) 3906 218</div>
      </div>
    </div>
  </header>
  <ul class="nav">
    <li class="active">Home</li><li>About Us</li><li>Services</li><li>Reservation</li><li>Spa</li><li>Blog</li><li>Contact</li>
  </ul>
  <section class="hero" role="img" aria-label="Woman relaxing with a flower in her hair during a back massage">
    <div class="hero-caption">
      <div class="hero-title">Coral Cove <span>Massage Centers</span></div>
      <p class="hero-text">Sed ut perspiciatis unde omnis iste natus error sit voluptatem accusantium doloremque laudantium, totam rem aperiam,</p>
    </div>
  </section>

  <div class="services">
    <div class="service">
      <div class="photo" role="img" aria-label="Herbal compress massage in a green garden" style="background:linear-gradient(135deg,#1f5e22 0%,#4f8a2e 45%,#c9a58a 100%)"></div>
      <div class="label">HERBAL MASSAGE</div>
      <span class="go"><svg width="15" height="15" viewBox="0 0 15 15"><path d="M6 4.5l3 3-3 3" fill="none" stroke="#fff" stroke-width="1.6"/></svg></span>
    </div>
    <div class="service">
      <div class="photo" role="img" aria-label="Foot massage with pink lotus flowers" style="background:linear-gradient(135deg,#e9d7c2 0%,#e2a58f 50%,#d9566a 100%)"></div>
      <div class="label">FOOT MASSAGE</div>
      <span class="go"><svg width="15" height="15" viewBox="0 0 15 15"><path d="M6 4.5l3 3-3 3" fill="none" stroke="#fff" stroke-width="1.6"/></svg></span>
    </div>
    <div class="service">
      <div class="photo" role="img" aria-label="Full body shoulder massage" style="background:linear-gradient(135deg,#d8bfae 0%,#c79377 50%,#efe6e0 100%)"></div>
      <div class="label">FULL BODY MASSAGE</div>
      <span class="go"><svg width="15" height="15" viewBox="0 0 15 15"><path d="M6 4.5l3 3-3 3" fill="none" stroke="#fff" stroke-width="1.6"/></svg></span>
    </div>
  </div>

  <section class="welcome">
    <h1>Welcome to <span class="b">Coral Cove</span> <span class="r">Massage</span> Centres</h1>
    <p>Lorem ipsum dolor sit amet, consectetur adipiscing elit, sed do eiusmod tempor incididunt ut labore et dolore magna aliqua. Ut enim ad minim veniam, quis nostrud exercitation ullamco laboris nisi ut aliquip ex ea commodo consequat. Duis aute irure dolor in reprehenderit in voluptate velit esse cillum dolore eu fugiat nulla pariatur. Excepteur sint occaecat cupidatat non proident, sunt in culpa qui officia deserunt mollit anim id est laborum Sed ut perspiciatis unde omnis iste natus error sit voluptatem accusantium .</p>
  </section>
  <span class="btn read-more">Read More</span>

  <form class="booking">
    <h2>Book an Apointment</h2>
    <div class="field">Name</div>
    <div class="field">Email address</div>
    <div class="field msg">Enter your Massage</div>
    <div class="btn submit">Submit</div>
  </form>
</div>

<svg class="wave" viewBox="0 0 884 1200" aria-hidden="true">
  <path d="M0 920 C120 985 220 1000 330 998 C480 995 600 955 720 962 C800 968 850 995 884 1015 L884 1200 L0 1200 Z" fill="#313131"/>
  <path d="M0 920 C120 985 220 1000 330 998 C480 995 600 955 720 962 C800 968 850 995 884 1015" fill="none" stroke="#e8232a" stroke-width="3"/>
</svg>

<footer class="footer">
  <div class="col" style="left:0">
    <h3>QUICK LINK</h3>
    <ul class="links"><li>HOME</li><li>BLOG</li><li>ABOUT US</li><li>CONTACT</li><li>SERVICES</li><li>RESERVATION</li><li>SPA</li></ul>
  </div>
  <div class="col" style="left:252px">
    <h3>CONTACT DETAILS</h3>
    <p style="padding-left:2px">14 HARBOUR LANE, SEAVIEW TRADE<br>PARK , SEAVIEW, WESTSHIRE<br>+44(0)1632960481<br>hello@coralcovemassage.com</p>
  </div>
  <div class="col" style="left:549px;width:188px">
    <h3>SUBSCRIBE TO NEWSLETTER</h3>
    <p style="padding-left:2px;line-height:13.5px">Drop your email address below to<br>receive Coupons &amp; Promos</p>
    <div class="news-input"></div>
    <div class="news-go"><svg width="23" height="28" viewBox="0 0 23 28"><path d="M9 8l6 6-6 6" fill="none" stroke="#fff" stroke-width="2.5"/></svg></div>
    <div class="radios"><span><i class="radio on"></i>Subscribe</span><span><i class="radio"></i>UnSubscribe</span></div>
  </div>
</footer>
<div class="rule"></div>
<div class="copy">© 2014 coral cove massage centers.All right reserved</div>
<div class="social" aria-label="Social links"><span></span><span></span><span></span><span></span></div>
</body>
</html>
```